Disease outbreak warning

I need a flyer that explains to hunters how to act as frontline responders to potential disease outbreaks in wildlife populations. In this case the disease is African Swine Fever. We need an at a glance style with plenty of colour and that’s very easy to read.

I HAVE ATTACHED SOME EXISTING FLYERS FROM OVERSEAS ETC THAT CONTAIN SOME OF THE RELEVANT INFO. THEY ARE TO BE USED AS A GUIDE ONLY.
Updates

Need to see some more options. We have some that can be developed successfully but we’d like to see some more options that will suit a national campaign.

Target Market(s)

Australian hunters encountering wild pigs. Typical age is from 18 to 32 but can be older. Male or female.

Colors

Designer to choose colors to be used in the design.

Requirements
Must have
• The KVRTE logo (supplied). It should be relatively small at the bottom of the page. Plus we need room for two or three other logos that can be overprinted on the project if required.
• Must have information for hunters as the main focus.
Nice to have
• A double sided flyer.
Should not have
• US spelling.

```html
<!DOCTYPE html>
<html lang="en-AU">
<head>
<meta charset="utf-8">
<title>ASF Outbreak Flyer – What To Do</title>
<link rel="stylesheet" href="https://fonts.googleapis.com/css2?family=Oswald:wght@300;400;600&family=Open+Sans:wght@400;600&display=swap">
<style>
  :root {
    --backdrop: #e8e8e8;
    --paper: #ffffff;
    --ink: #111111;
    --salmon: #ff7070;
    --red: #e8323c;
    --red-deep: #e31b23;
    --red-bright: #ff3b45;
    --slate: #526079;
    --navy: #26344f;
    --white: #ffffff;
  }
  * { margin: 0; padding: 0; box-sizing: border-box; }
  html, body { width: 1200px; height: 1200px; overflow: hidden; background: var(--backdrop); }
  .flyer {
    position: absolute; left: 171px; top: 45px;
    width: 857px; height: 1109px;
    background: var(--paper);
    font-family: "Open Sans", Arial, sans-serif;
    overflow: hidden;
  }
  .block { position: absolute; }
  .accent-top { left: 0; top: 0; width: 111px; height: 198px; background: var(--salmon); }
  .accent-steps { left: 0; top: 198px; width: 111px; height: 489px; background: var(--red); }
  .accent-callout { left: 0; top: 687px; width: 111px; height: 316px; background: var(--red-deep); }
  .steps-panel { left: 111px; top: 198px; width: 746px; height: 489px; background: var(--slate); }
  .callout-panel { left: 111px; top: 687px; width: 746px; height: 316px; background: var(--navy); }

  .hero-art {
    position: absolute; left: 440px; top: 42px; width: 417px; height: 405px;
    background: radial-gradient(ellipse at 55% 50%, #4a5872 0%, #3f4c63 55%, rgba(82,96,121,0) 75%);
  }
  .hero-tag {
    position: absolute; left: 598px; top: 112px;
    font-family: "Oswald", Impact, sans-serif; font-weight: 600;
    font-size: 92px; line-height: 1; color: var(--red-bright); letter-spacing: 2px;
    opacity: 0.9;
  }

  .title {
    position: absolute; left: 53px; top: 42px;
    font-family: "Oswald", Impact, sans-serif; font-weight: 600;
    font-size: 104px; line-height: 1; color: var(--ink); letter-spacing: -1px;
    transform: scaleX(0.82); transform-origin: left top;
  }
  .subtitle {
    position: absolute; left: 58px; top: 145px;
    font-size: 23px; color: var(--ink); letter-spacing: 0.2px;
  }

  .step-num {
    position: absolute; left: 40px;
    font-family: "Oswald", Impact, sans-serif; font-weight: 400;
    font-size: 62px; line-height: 1; color: var(--white);
  }
  .step-text {
    position: absolute; left: 122px; width: 320px;
    font-size: 20px; line-height: 30px; color: var(--white);
  }
  .about {
    position: absolute; left: 484px; top: 457px; width: 340px;
    font-size: 20px; line-height: 29.5px; color: var(--white);
  }
  .about strong { font-weight: 600; }

  .callout-head {
    position: absolute; left: 138px; top: 710px;
    font-family: "Oswald", Impact, sans-serif; font-weight: 400;
    font-size: 72px; line-height: 76px; color: var(--red-bright);
    transform: scaleX(0.82); transform-origin: left top; white-space: nowrap;
  }
  .callout-sub {
    position: absolute; left: 141px; top: 946px;
    font-size: 20px; color: var(--white);
  }

  .more-info {
    position: absolute; left: 37px; top: 1035px;
    font-size: 20px; color: var(--ink);
  }
  .client-mark {
    position: absolute; left: 548px; top: 1040px;
    display: flex; align-items: center; gap: 8px;
    font-size: 18px; font-weight: 600; color: var(--navy);
  }
  .client-mark .dot { width: 30px; height: 30px; border-radius: 50%; background: var(--navy); }
</style>
</head>
<body>
  <main class="flyer">
    <div class="block accent-top"></div>
    <div class="block accent-steps"></div>
    <div class="block accent-callout"></div>
    <div class="block steps-panel"></div>
    <div class="block callout-panel"></div>

    <div class="hero-art" role="img" aria-label="Engraved-style illustration of a wild boar standing on grass"></div>
    <div class="hero-tag">ASF</div>

    <h1 class="title">WHAT TO DO?</h1>
    <p class="subtitle">IN ASF OUTBREAKS IN WILDLIFE</p>

    <div class="step-num" style="top:220px">1.</div>
    <p class="step-text" style="top:225px">clean and disinfect all equipment on the area.</p>

    <div class="step-num" style="top:338px">2.</div>
    <p class="step-text" style="top:325px">clean and bag all carcasses before leaving the hunting area.</p>

    <div class="step-num" style="top:458px">3.</div>
    <p class="step-text" style="top:440px">Report any signs of sick or dead pigs by calling Emergency Animal Disease hotline on 1800 420 317</p>

    <div class="step-num" style="top:578px">4.</div>
    <p class="step-text" style="top:578px">Respect all quarantines and restrictions that are in place.</p>

    <p class="about">African swine fever (ASF) is a <strong>highly contagious</strong> haemorrhagic viral disease of domestic and wild pigs, which is responsible for serious economic and production losses.</p>

    <h2 class="callout-head">HUNTERS DONT BE THE<br>CARRIER OF DEADLY<br>PIG DESEASE!</h2>
    <p class="callout-sub">Be resposible and act appropriately.</p>

    <p class="more-info">for more info visit:</p>
    <div class="client-mark"><span class="dot"></span>KVRTE</div>
  </main>
</body>
</html>
```